Full Page Magazine Add for Bulb Recycler

We need ad that to promote our expertise, capabilities and value in industry trade magazines. We want clean, clear look feel to reflect our impact on the environment.

Target Market(s)

Industry -- Electricians -- Environmental Services

Font styles to use
Sans Serif

Colors
eef8f9

Requirements
Must have
• I have included instructions outlining all details of must / haves -- ALSO) there are 4 jpegs of LOOK/FEEL Examples that we like -- as reference -- FILE names are EXAMPLE
Nice to have
• Welcome guidance on helping with logo transition -- we're moving from Beacon Salvage -- to Kind to the Soil -- but for now -- need to display both -- we've just put an IS in between -- but if you have ideas definitely WELCOME

```html
<!DOCTYPE html>
<html lang="en">
<head>
<meta charset="utf-8">
<title>Beacon Salvage – Protecting the Environment</title>
<link href="https://fonts.googleapis.com/css2?family=Poppins:wght@500;600&family=Questrial&display=swap" rel="stylesheet">
<style>
  :root {
    --navy: #1f3f7e;
    --blue: #1d4f91;
    --green: #3fb36a;
    --green-light: #8fd19e;
    --lime: #c9e27a;
    --ink: #1f1f1f;
    --paper: #f2f3f5;
    --photo-grey: #b9bec6;
    --yellow: #f2e33a;
  }
  * { margin: 0; padding: 0; box-sizing: border-box; }
  html, body { width: 927px; height: 1200px; overflow: hidden; background: var(--paper); }
  .ad { position: relative; width: 927px; height: 1200px; background: var(--paper); font-family: "Questrial", sans-serif; color: var(--ink); }
  .band { position: absolute; left: 0; width: 927px; }
  .band-top { top: 0; height: 160px; }
  .band-bottom { bottom: 0; height: 170px; }

  .headline { position: absolute; top: 160px; left: 0; width: 927px; text-align: center; }
  .headline h1 { font-family: "Poppins", sans-serif; font-weight: 600; font-size: 50px; line-height: 1; color: var(--blue); letter-spacing: -0.5px; }
  .headline h2 { font-family: "Poppins", sans-serif; font-weight: 500; font-size: 33px; line-height: 1; color: #2d2d2d; margin-top: 10px; }

  .feature { position: absolute; width: 266px; }
  .feature-photo { height: 175px; }
  .feature-label { height: 54px; color: #fff; font-family: "Questrial", sans-serif; font-size: 30px; line-height: 29px; display: flex; align-items: center; justify-content: center; text-align: center; }
  .feature-label.tall { height: 80px; }
  .label-green { background: var(--green); }
  .label-blue { background: var(--blue); justify-content: flex-start; padding-left: 42px; text-align: left; }
  .label-blue.centered { justify-content: center; padding-left: 0; text-align: center; }
  .feature p { font-size: 14.3px; line-height: 18.2px; text-align: justify; padding: 6px 4px 0 4px; }

  .photo-plant { background: linear-gradient(160deg, #5b7fa6 0%, #9a8f76 55%, #6f6a62 100%); }
  .photo-tubes { background: linear-gradient(180deg, #e9e9e6 0%, #cfcfc9 60%, #bfbfb8 100%); }
  .photo-truck { background: linear-gradient(180deg, #cfcfd2 0%, #e8e8ea 55%, #9a9a9a 100%); }
  .photo-batteries { background: linear-gradient(160deg, #d7dde4 0%, #e7784a 50%, #6fb8c8 100%); }
  .photo-exit { background: linear-gradient(160deg, #d9d9d9 0%, #e8e8e8 50%, #c44 75%, #1f5f3a 100%); }

  .map { position: absolute; left: 608px; top: 703px; width: 300px; height: 205px; background: linear-gradient(180deg, #c8c8c8, #b3b3b3); border-radius: 24px 40px 30px 60px; }

  .brand { position: absolute; left: 620px; top: 918px; width: 270px; }
  .brand-main { display: flex; align-items: center; gap: 10px; }
  .brand-dot { width: 44px; height: 44px; border-radius: 50%; background: var(--yellow); flex: none; }
  .brand-name { font-family: "Poppins", sans-serif; font-weight: 600; font-size: 34px; line-height: 38px; color: var(--blue); }
  .brand-next { display: flex; align-items: center; gap: 14px; margin-top: 18px; }
  .brand-is { font-family: "Poppins", sans-serif; font-weight: 600; font-size: 24px; color: var(--blue); }
  .brand-new { font-family: "Poppins", sans-serif; font-weight: 600; font-size: 28px; color: var(--green); }
</style>
</head>
<body>
<div class="ad">
  <svg class="band band-top" viewBox="0 0 927 160" preserveAspectRatio="none" aria-hidden="true">
    <defs>
      <linearGradient id="greenTop" x1="0" x2="1"><stop offset="0" stop-color="#3fb36a"/><stop offset="1" stop-color="#a9dcb6"/></linearGradient>
    </defs>
    <polygon points="0,0 927,0 927,8 463,66 0,22" fill="var(--navy)"/>
    <polygon points="0,22 463,66 927,8 927,22 463,86 0,40" fill="var(--lime)"/>
    <polygon points="0,40 463,86 927,22 927,72 463,154 0,92" fill="url(#greenTop)"/>
  </svg>

  <header class="headline">
    <h1>Protecting the Environment</h1>
    <h2>and Assuring Your Compliance</h2>
  </header>

  <section class="feature" style="left:52px; top:293px;">
    <div class="feature-photo photo-plant" role="img" aria-label="Workers sorting lamps at a recycling processing machine"></div>
    <div class="feature-label label-green">Technology</div>
    <p>Our processing facilities are equipped with the most advanced recycling equipment in the industry. We safely recycle millions of bulbs every year.</p>
  </section>

  <section class="feature" style="left:329px; top:293px;">
    <div class="feature-photo photo-tubes" role="img" aria-label="Stack of used fluorescent tubes awaiting recycling"></div>
    <div class="feature-label label-blue" style="margin-top:-26px; height:72px;">Reclaiming<br>Resources</div>
    <p>Our processing facilities are equipped with the most advanced recycling equipment in the industry. We safely recycle millions of bulbs every year.</p>
  </section>

  <section class="feature" style="left:605px; top:293px;">
    <div class="feature-photo photo-truck" role="img" aria-label="White company box truck with a driver standing beside it"></div>
    <div class="feature-label label-green">Nationwide</div>
    <p>We provide processing and licensed pick up of hazardous and universal waste by pallet-full or truck load for many of the largest and most well-known companies, institutions and agencies in the country.</p>
  </section>

  <section class="feature" style="left:53px; top:658px;">
    <div class="feature-photo photo-batteries" role="img" aria-label="Close-up of colourful household batteries"></div>
    <div class="feature-label tall label-blue centered">Fast Easy<br>Mail-In Recycling</div>
    <p>Kind to the Soil Recycling kits ensure you have what you need when you need to properly manage your small quantity batteries, bulbs, ballasts, exit signs and more. Pre-paid shipping and processing. Kits shipped within 24 hours.</p>
  </section>

  <section class="feature" style="left:331px; top:658px;">
    <div class="feature-photo photo-exit" role="img" aria-label="Red and green illuminated exit signs"></div>
    <div class="feature-label tall label-green">Egress<br>Safety Solutions</div>
    <p>In addition to fully-managed retrofit and recycle of tritium exit sign we offer a complete line of energy and maintenance-free phosphorescent exit signs and safety marking.</p>
  </section>

  <div class="map" role="img" aria-label="Map of the United States marking facility locations"></div>

  <div class="brand">
    <div class="brand-main">
      <span class="brand-dot"></span>
      <span class="brand-name">Beacon Salvage</span>
    </div>
    <div class="brand-next">
      <span class="brand-is">IS</span>
      <span class="brand-new">Kind to the Soil</span>
    </div>
  </div>

  <svg class="band band-bottom" viewBox="0 0 927 170" preserveAspectRatio="none" aria-hidden="true">
    <defs>
      <linearGradient id="greenBottom" x1="0" x2="1"><stop offset="0" stop-color="#3fb36a"/><stop offset="1" stop-color="#a9dcb6"/></linearGradient>
    </defs>
    <polygon points="0,60 463,10 927,50 927,110 463,80 0,120" fill="url(#greenBottom)"/>
    <polygon points="0,120 463,80 927,110 927,122 463,96 0,134" fill="var(--lime)"/>
    <polygon points="0,146 463,112 927,134 927,170 0,170" fill="var(--navy)"/>
  </svg>
</div>
</body>
</html>
```